We specialize in pizza, pasta and salads and are now offering TAKE & BAKE and GRAB & GO ...

Looking for either a 8.5" x 11" or similar for a instore display. WILL BE ON A SWIVELING HOLDER to catch customers attention.

**THIS IS A DOUBLE SIDED PRINT**

ONE SIDE will consist of WHAT'S FOR DINNER TONIGHT? and the following:
* Take & Bake"
* "Baked Pasta"
* Freshly made in house
* Lasagna
$13.50
- please include attached closeup picture and logo

THE OTHER SIDE will consist of
mini charcutier board.
* snack size charcutier delight *
* Enjoy the flavors of gourmet snacking, all in one convenient box!

PRICE $8.99

Winning design will be commissioned to design labels for "grab and go" for take and bake pasta, charcuterie box, pasta salads, candy etc.

Thank you and please do not hesitate to ask any questions.

www.calderipizza.ca
www.fernloop.ca
Logo to be interchanged as they are affiliated meaning FernLoop is a brand within Calderi pizza.

Target Market(s)

our target market is customers who have already entered our business. This is to upsel

Industry/Entity Type

We are in a self serve enviroment and target business people

Requirements
Must have
• must be clean and catchy. We are located in a professional business community.
Nice to have
• Must be appealing, appetizing and utilize our website colors
Should not have
• should not have any carton drawings and not be cluttered (busy)

```html
<!DOCTYPE html>
<html lang="en">
<head>
<meta charset="utf-8">
<title>Calderi Pizza – In-store Flyer</title>
<link rel="stylesheet" href="https://fonts.googleapis.com/css2?family=Oswald:wght@300;400;600;700&family=Montserrat:wght@400;500&family=Josefin+Sans:wght@300&display=swap">
<style>
  :root {
    --backdrop: #707070;
    --paper: #ffffff;
    --paper-grey: #ececec;
    --ink: #231f20;
    --panel: #2c2b2b;
    --red: #c1272d;
    --swoosh: #d9d9d9;
    --white: #ffffff;
  }
  * { margin: 0; padding: 0; box-sizing: border-box; }
  html, body { width: 1200px; height: 2408px; overflow: hidden; }
  body { background: var(--backdrop); position: relative; }

  .flyer {
    position: absolute;
    left: 41px; top: 413px;
    width: 932px; height: 1318px;
    transform: scale(1.2);
    transform-origin: 0 0;
    background: var(--paper);
    overflow: hidden;
    font-family: "Montserrat", sans-serif;
    box-shadow: 0 20px 40px rgba(0,0,0,.35);
  }
  .flyer-art { position: absolute; inset: 0; width: 932px; height: 1318px; }
  .flyer > .txt { position: absolute; white-space: nowrap; }

  .brand {
    left: 0; width: 932px; top: 38px; text-align: center;
    font-family: "Josefin Sans", sans-serif; font-weight: 300;
    font-size: 92px; letter-spacing: 2px; color: var(--ink); line-height: 1;
  }

  .headline-top {
    left: 0; width: 932px; top: 246px; text-align: center; padding-right: 60px;
    font-family: "Oswald", sans-serif; font-weight: 300;
    font-size: 104px; line-height: 1; color: var(--red);
  }
  .headline-main {
    left: 0; width: 932px; top: 348px; text-align: center; padding-right: 40px;
    font-family: "Oswald", sans-serif; font-weight: 700;
    font-size: 104px; line-height: 1; color: var(--white); letter-spacing: -1px;
  }

  .checklist { list-style: none; position: absolute; left: 110px; }
  .checklist li {
    display: flex; align-items: center; gap: 22px;
    font-size: 30px; line-height: 42.5px; letter-spacing: 1px;
  }
  .checklist--dinner { top: 488px; color: var(--white); }
  .checklist--snack { top: 1096px; color: var(--ink); }
  .checklist--snack li { align-items: flex-start; line-height: 42px; }
  .checklist--snack li .tick { margin-top: 7px; }
  .tick { width: 30px; height: 30px; flex: none; }

  .price-pill {
    position: absolute; left: 110px; width: 368px; height: 50px;
    background: var(--red); border: 2px solid var(--white); border-radius: 25px;
    box-shadow: 0 0 0 1px var(--red);
    color: var(--white); text-align: center;
    font-family: "Oswald", sans-serif; font-weight: 300; font-size: 38px; line-height: 46px;
  }
  .price-pill b { font-weight: 600; }
  .price-pill--dinner { top: 668px; }
  .price-pill--snack { top: 1182px; }

  .product-title {
    left: 0; width: 932px; top: 836px; text-align: center;
    font-family: "Oswald", sans-serif; font-size: 100px; line-height: 1.05; color: var(--ink);
  }
  .product-title .light { font-weight: 300; }
  .product-title .bold { font-weight: 700; color: var(--red); }

  .product-sub {
    left: 0; width: 932px; top: 944px; text-align: center;
    font-family: "Oswald", sans-serif; font-weight: 700; font-size: 54px;
    letter-spacing: 22px; line-height: 1; color: var(--ink); padding-left: 22px;
  }

  .tagline {
    left: 0; width: 932px; top: 1020px; height: 60px; text-align: center;
    font-family: "Oswald", sans-serif; font-weight: 400; font-size: 44px; line-height: 60px;
    color: var(--white);
  }

  .website {
    left: 584px; top: 1252px;
    font-size: 22px; letter-spacing: .5px; color: var(--white);
  }
</style>
</head>
<body>
<main class="flyer">
  <svg class="flyer-art" viewBox="0 0 932 1318" aria-hidden="false">
    <defs>
      <linearGradient id="panelTone" x1="0" y1="0" x2="1" y2="1">
        <stop offset="0" stop-color="#3a3432"/>
        <stop offset=".5" stop-color="#2b2a2a"/>
        <stop offset="1" stop-color="#353535"/>
      </linearGradient>
      <radialGradient id="cheeseTone" cx=".45" cy=".45" r=".6">
        <stop offset="0" stop-color="#d9b98a"/>
        <stop offset=".45" stop-color="#b97a32"/>
        <stop offset="1" stop-color="#5a3512"/>
      </radialGradient>
    </defs>

    <!-- lower grey field -->
    <rect class="lower-field" x="0" y="1079" width="932" height="239" fill="var(--paper-grey)"/>

    <!-- dinner panel -->
    <path d="M0 290 Q 420 162 932 176" fill="none" stroke="var(--swoosh)" stroke-width="14"/>
    <path d="M0 298 Q 420 170 932 184" fill="none" stroke="var(--ink)" stroke-width="5"/>
    <g role="img" aria-label="Darkened close-up photo of baked pasta with stretching cheese">
      <path d="M0 308 Q 420 180 932 194 L932 585 Q 560 765 0 748 Z" fill="url(#panelTone)"/>
    </g>
    <path d="M0 308 Q 420 180 932 194" fill="none" stroke="var(--red)" stroke-width="8"/>
    <path d="M0 752 Q 560 770 932 588" fill="none" stroke="var(--ink)" stroke-width="4"/>
    <path d="M0 764 Q 560 782 932 600" fill="none" stroke="var(--red)" stroke-width="8"/>
    <path d="M0 782 Q 560 800 932 618" fill="none" stroke="var(--swoosh)" stroke-width="10"/>

    <!-- feature photo -->
    <circle cx="734" cy="644" r="164" fill="var(--ink)"/>
    <circle cx="734" cy="644" r="154" fill="var(--white)"/>
    <g role="img" aria-label="Close-up photo of a cheesy baked pasta slice">
      <circle cx="736" cy="644" r="146" fill="url(#cheeseTone)"/>
    </g>
    <polygon points="538,546 604,489 664,636" fill="var(--red)"/>

    <!-- BOARD rules -->
    <rect x="186" y="972" width="150" height="4" fill="var(--red)"/>
    <rect x="596" y="972" width="150" height="4" fill="var(--red)"/>

    <!-- black tagline band -->
    <rect x="0" y="1017" width="932" height="62" fill="var(--ink)"/>

    <!-- bottom shapes -->
    <path d="M170 1318 Q 250 1276 330 1272 L500 1272 Q 470 1300 460 1318 Z" fill="var(--red)"/>
    <path d="M250 1318 Q 330 1262 420 1260 L560 1262 Q 520 1290 500 1318 Z" fill="var(--ink)"/>
    <path d="M430 1318 Q 470 1240 590 1240 L932 1240 L932 1318 Z" fill="var(--red)"/>

    <!-- accent triangles -->
    <polygon points="40,1000 92,962 124,1070" fill="var(--red)"/>
    <polygon points="794,972 822,958 826,995" fill="var(--ink)"/>
    <polygon points="856,956 878,946 866,972" fill="var(--red)"/>
    <polygon points="684,1196 728,1210 704,1170" fill="var(--ink)"/>
    <polygon points="828,1120 886,1158 802,1230" fill="var(--red)"/>
    <polygon points="44,1256 132,1262 60,1302" fill="var(--ink)"/>
  </svg>

  <div class="txt brand">CALDERI PIZZA</div>

  <h1 class="txt headline-top">WHAT'S FOR</h1>
  <div class="txt headline-main">DINNER TONIGHT?</div>

  <ul class="checklist checklist--dinner">
    <li><svg class="tick" viewBox="0 0 30 30"><rect x="1" y="1" width="28" height="28" rx="3" fill="#c1272d" stroke="#fff" stroke-width="2"/><path d="M7 15 L13 21 L23 8" fill="none" stroke="#fff" stroke-width="4"/></svg>Take &amp; Bake</li>
    <li><svg class="tick" viewBox="0 0 30 30"><rect x="1" y="1" width="28" height="28" rx="3" fill="#c1272d" stroke="#fff" stroke-width="2"/><path d="M7 15 L13 21 L23 8" fill="none" stroke="#fff" stroke-width="4"/></svg>Baked Pasta</li>
    <li><svg class="tick" viewBox="0 0 30 30"><rect x="1" y="1" width="28" height="28" rx="3" fill="#c1272d" stroke="#fff" stroke-width="2"/><path d="M7 15 L13 21 L23 8" fill="none" stroke="#fff" stroke-width="4"/></svg>Freshly made in house</li>
    <li><svg class="tick" viewBox="0 0 30 30"><rect x="1" y="1" width="28" height="28" rx="3" fill="#c1272d" stroke="#fff" stroke-width="2"/><path d="M7 15 L13 21 L23 8" fill="none" stroke="#fff" stroke-width="4"/></svg>Lasagna</li>
  </ul>
  <div class="price-pill price-pill--dinner">PRICE: <b>$13.50</b></div>

  <h2 class="txt product-title"><span class="light">MINI</span> <span class="bold">CHARCUTERIE</span></h2>
  <div class="txt product-sub">BOARD</div>
  <div class="txt tagline">SNACK SIZE CHARCUTERIE DELIGHT</div>

  <ul class="checklist checklist--snack">
    <li><svg class="tick" viewBox="0 0 30 30"><rect x="1" y="1" width="28" height="28" rx="3" fill="#c1272d" stroke="#fff" stroke-width="2"/><path d="M7 15 L13 21 L23 8" fill="none" stroke="#fff" stroke-width="4"/></svg><span>Enjoy the flavors of gourment snacking,<br>all in one convenient box!</span></li>
  </ul>
  <div class="price-pill price-pill--snack">PRICE: <b>$8.99</b></div>

  <div class="txt website">www.calderipizza.ca</div>
</main>
</body>
</html>
```